Redesign www.KORVADO.ch - Storefront Web-Shop - Storytelling

Redesign of existing Storefront Web-page of KOR-VADO.ch.
Please carefully review both enclosed documents. The annotated notes explain the expected design direction and priorities.

```html
<!DOCTYPE html>
<html lang="en">
<head>
<meta charset="utf-8">
<title>KOR-VADO – Handmade Scarves</title>
<link rel="stylesheet" href="https://fonts.googleapis.com/css2?family=Oswald:wght@500;600&family=Poppins:wght@400;500;600&display=swap">
<style>
:root{
  --page:#f4f3f0;
  --band:#ecebe7;
  --card:#f0efec;
  --ink:#4a4d52;
  --text:#3c3e42;
  --muted:#6b6d71;
  --white:#ffffff;
  --blush:#f8ddd5;
  --star:#f0a830;
  --heart:#e0322f;
  --footer:#4a4d52;
}
*{box-sizing:border-box;margin:0;padding:0}
html,body{width:1200px;height:4237px;overflow:hidden}
body{background:var(--page);font-family:"Poppins",sans-serif;color:var(--text);position:relative}
.abs{position:absolute}
.head{font-family:"Oswald",sans-serif;font-weight:600;color:var(--ink);text-transform:uppercase;letter-spacing:.2px}
.btn{position:absolute;background:var(--ink);color:var(--white);font-size:12px;font-weight:500;display:flex;align-items:center;justify-content:center;gap:8px;text-transform:uppercase}
.btn svg{width:12px;height:12px}

/* header */
.site-header{position:absolute;left:0;top:0;width:1200px;height:62px;background:var(--page)}
.menu{left:150px;top:24px;display:flex;align-items:center;gap:8px;font-size:12px;font-weight:500}
.brand{left:500px;top:0;width:200px;height:62px;display:flex;align-items:center;justify-content:center;gap:8px;font-family:"Poppins",sans-serif;font-weight:600;font-size:15px;color:var(--ink)}
.brand i{display:block;width:10px;height:10px;background:var(--ink)}
.header-icons{left:958px;top:20px;display:flex;gap:16px}
.header-icons svg{width:22px;height:22px}

/* hero */
.hero-panel{position:absolute;top:62px;height:601px;width:277px}
.hero-card{left:199px;top:482px;width:809px;height:181px;background:var(--page);text-align:center}
.hero-card h1{font-size:32px;line-height:40px;margin-top:42px}
.hero-card p{font-size:11px;margin-top:10px}

/* features */
.feature{position:absolute;top:756px;width:160px;text-align:center;font-size:12px;line-height:15px}
.feature .ico{width:69px;height:69px;margin:0 auto 22px;background:var(--white);display:flex;align-items:center;justify-content:center}
.feature svg{width:40px;height:40px}

/* designer */
.designer-photo{left:49px;top:948px;width:485px;height:456px;background:linear-gradient(160deg,#4e4f52,#2e2f31)}
.designer-text{left:580px;top:1052px;width:498px;text-align:center}
.designer-text .eyebrow{font-size:15px;font-weight:500;color:var(--ink)}
.designer-text h2{font-size:32px;line-height:36px}
.designer-text p{font-size:18px;line-height:28px;margin-top:14px}

/* selection */
.selection{left:0;top:1485px;width:1200px;height:915px;background:var(--band)}
.section-title{position:absolute;left:0;width:1200px;text-align:center;font-size:32px}
.product{position:absolute;width:219px;height:314px;background:var(--card);text-align:center;font-size:12px;font-weight:500;color:var(--ink)}
.product .shot{height:183px;background:var(--white);display:flex;justify-content:center;align-items:flex-end}
.product .shot span{display:block;width:70px;height:160px;border-radius:34px 34px 6px 6px}
.product .name{margin-top:20px;line-height:19px;text-transform:uppercase}
.product .price{font-weight:600;margin-top:4px}
.product .cart{font-weight:600;margin-top:6px;display:flex;justify-content:center;align-items:center;gap:5px;text-transform:uppercase}
.product .cart svg{width:13px;height:13px}

/* tiles */
.tile{position:absolute;top:2410px;height:446px}
.tile h3{position:absolute;font-size:22px}
.tile p{position:absolute;font-size:15px;line-height:22px;width:270px}

/* uniqueness */
.unique{left:16px;top:2867px;width:1169px;height:446px;background:var(--blush)}
.unique-word{left:290px;top:2990px;width:620px;text-align:center;font-size:122px;line-height:150px;letter-spacing:-2px}
.unique-note{left:779px;top:3138px;width:230px;font-size:15px;line-height:22px}

/* reviews */
.review{position:absolute;top:3452px;width:296px;height:135px;background:var(--white);padding:28px 22px 0 22px;display:flex;gap:14px;box-shadow:0 2px 8px rgba(0,0,0,.03)}
.avatar{width:52px;height:52px;border-radius:50%;flex:none}
.review b{display:block;font-family:"Oswald",sans-serif;font-weight:500;font-size:12px;color:var(--ink);text-transform:uppercase}
.stars{display:flex;align-items:center;gap:2px;font-size:10px;color:var(--muted);margin:3px 0 6px}
.stars svg{width:10px;height:10px}
.review p{font-size:12px;line-height:16px;color:var(--muted)}
.dots{left:582px;top:3609px;display:flex;gap:7px}
.dots i{width:7px;height:7px;border-radius:50%;background:#cfcfcf}
.dots i:first-child{background:var(--ink)}

/* community */
.community-text{left:0;top:3729px;width:1200px;text-align:center;font-size:15px;line-height:22px}
.email{left:332px;top:3791px;width:536px;height:43px;border:1.5px solid #c9c9c9;background:var(--white);display:flex;align-items:center;justify-content:space-between;padding:0 18px 0 28px;font-size:12px;color:var(--muted)}

/* footer */
.footer{left:0;top:3926px;width:1200px;height:311px;background:var(--footer);color:var(--white)}
.footer-brand{left:0;top:3994px;width:1200px;display:flex;justify-content:center;align-items:center;gap:8px;font-family:"Poppins",sans-serif;font-weight:600;font-size:15px;color:var(--white)}
.footer-brand i{display:block;width:10px;height:10px;background:var(--white)}
.footer-title{left:0;top:4034px;width:1200px;text-align:center;font-size:32px;color:var(--white)}
.footer-btn{left:496px;top:4084px;width:209px;height:36px;background:var(--white);color:var(--ink);font-size:12px;font-weight:500;display:flex;align-items:center;justify-content:center;gap:8px;text-transform:uppercase}
.footer-links{left:0;top:4157px;width:1200px;display:flex;justify-content:center;gap:22px;font-size:10px;color:#e6e6e6}
.copyright{left:150px;top:4200px;font-size:10px;color:#e6e6e6}
.pay{left:881px;top:4196px;display:flex;gap:6px}
.pay span{width:32px;height:20px;border-radius:3px;display:block}
.chat{left:1108px;top:4146px;width:36px;height:36px;border-radius:50%;background:#25b34a;display:flex;align-items:center;justify-content:center}
</style>
</head>
<body>

<header class="site-header">
  <div class="abs menu">
    <svg width="18" height="12" viewBox="0 0 18 12"><path d="M0 1h18M0 6h12M0 11h18" stroke="#3c3e42" stroke-width="2"/></svg>MENU
  </div>
  <div class="abs brand"><i></i>KOR-VADO</div>
  <div class="abs header-icons">
    <svg viewBox="0 0 24 24" fill="none" stroke="#3c3e42" stroke-width="2"><circle cx="10" cy="10" r="6"/><path d="M15 15l5 5"/></svg>
    <svg viewBox="0 0 24 24" fill="none" stroke="#3c3e42" stroke-width="2"><path d="M5 8h14l-1 13H6z"/><path d="M9 8V6a3 3 0 016 0v2"/><circle cx="19" cy="19" r="4" fill="#e0322f" stroke="none"/></svg>
    <svg viewBox="0 0 24 24" fill="none" stroke="#3c3e42" stroke-width="2"><path d="M12 20s-8-5-8-11a4.5 4.5 0 018-3 4.5 4.5 0 018 3c0 6-8 11-8 11z"/></svg>
  </div>
</header>

<div class="hero-panel" style="left:49px;background:linear-gradient(160deg,#b5704e,#8a5a3f 60%,#c08a62)" role="img" aria-label="Close-up of a rust floral scarf with tassels"></div>
<div class="hero-panel" style="left:326px;background:linear-gradient(160deg,#4c5e5f,#394848 60%,#6b5a48)" role="img" aria-label="Teal dotted scarf with cream tassels"></div>
<div class="hero-panel" style="left:603px;background:linear-gradient(160deg,#a9876a,#8e6e55 60%,#6a5443)" role="img" aria-label="Tan dotted scarf with dark tassels"></div>
<div class="hero-panel" style="left:880px;width:274px;background:linear-gradient(160deg,#2a3350,#3e4a5e 50%,#a57f6e)" role="img" aria-label="Navy floral scarf with tassels"></div>
<div class="abs hero-card">
  <h1 class="head">Handmade unique pieces for<br>women with style.</h1>
  <p>Each KOR-VADO scarf is one of a kind – carefully crafted to add personality to your outfit.</p>
</div>
<div class="btn" style="left:513px;top:640px;width:173px;height:39px">Discover scarves <svg viewBox="0 0 12 12" fill="none" stroke="#fff" stroke-width="1.3"><path d="M1 6h10M7 2l4 4-4 4"/></svg></div>

<div class="feature" style="left:199px"><div class="ico"><svg viewBox="0 0 40 40" fill="none" stroke="#3c3e42" stroke-width="1.6"><path d="M8 24l10-12 6 4-8 10zM16 28c4 4 12 4 16-4l-6-4"/></svg></div>Handmade locally in<br>Switzerland</div>
<div class="feature" style="left:403px"><div class="ico"><svg viewBox="0 0 40 40" fill="none" stroke="#3c3e42" stroke-width="1.6"><path d="M10 12l3-2v12M26 8L14 32M24 22h5a2 2 0 010 4h-3 3a2 2 0 010 4h-5"/></svg></div>Only 1–3 pieces per<br>design</div>
<div class="feature" style="left:607px"><div class="ico"><svg viewBox="0 0 40 40" fill="none" stroke="#3c3e42" stroke-width="1.6"><path d="M12 10v20M16 10v20M20 10v20M24 10v20M28 10v20M10 14h20M10 19h20M10 24h20M10 28h20"/></svg></div>High-quality fabrics<br>without scratching</div>
<div class="feature" style="left:827px"><div class="ico"><svg viewBox="0 0 40 40" fill="none" stroke="#3c3e42" stroke-width="1.6"><path d="M8 26c6 0 10 4 16 2l8-4M12 20c6-2 12 0 16 2M16 8l1 3 3 1-3 1-1 3-1-3-3-1 3-1z"/></svg></div>Lightweight and suitable<br>for everyday use</div>

<div class="abs designer-photo" role="img" aria-label="Portrait of the designer seated, wearing a leather jacket and a plaid scarf"></div>
<div class="abs designer-text">
  <div class="eyebrow">KOR-VADO</div>
  <h2 class="head">Story Designer</h2>
  <p>Fabrics have been part of my life since childhood.<br>My grandmother and my mother created with their<br>hands – and this is exactly what I continue today.<br>I consciously take my time for each piece…</p>
</div>
<div class="btn" style="left:750px;top:1249px;width:154px;height:43px">View new pieces <svg viewBox="0 0 12 12" fill="none" stroke="#fff" stroke-width="1.3"><path d="M1 6h10M7 2l4 4-4 4"/></svg></div>

<section class="abs selection"></section>
<h2 class="head section-title" style="top:1562px">A selection for you <svg width="36" height="32" viewBox="0 0 24 22" style="vertical-align:-4px"><path d="M12 21S1 14 1 7a5.5 5.5 0 0111-2 5.5 5.5 0 0111 2c0 7-11 14-11 14z" fill="#e0322f"/></svg></h2>

<div class="product" style="left:150px;top:1618px"><div class="shot"><span role="img" aria-label="Cream knit top on a mannequin" style="background:linear-gradient(#b57a52 0 12%,#e8e0d2 12%)"></span></div><div class="name">Mirella triangular<br>scarf/small scarf</div><div class="price">CHF 39.00</div><div class="cart"><svg viewBox="0 0 14 14" fill="none" stroke="#4a4d52" stroke-width="1.3"><path d="M1 2h2l2 7h7l1-5H4"/><circle cx="6" cy="12" r="1"/><circle cx="11" cy="12" r="1"/></svg>Add to cart</div></div>
<div class="product" style="left:378px;top:1618px"><div class="shot"><span role="img" aria-label="Black scarf on a denim jacket" style="background:linear-gradient(#b57a52 0 12%,#2c2d30 12% 45%,#6f8fb3 45%)"></span></div><div class="name">Mirella triangular<br>scarf/small scarf</div><div class="price">CHF 39.00</div><div class="cart"><svg viewBox="0 0 14 14" fill="none" stroke="#4a4d52" stroke-width="1.3"><path d="M1 2h2l2 7h7l1-5H4"/><circle cx="6" cy="12" r="1"/><circle cx="11" cy="12" r="1"/></svg>Add to cart</div></div>
<div class="product" style="left:607px;top:1618px"><div class="shot"><span role="img" aria-label="Red floral scarf on a denim jacket" style="background:linear-gradient(#b57a52 0 12%,#c8453a 12% 45%,#6f8fb3 45%)"></span></div><div class="name">Mirella triangular<br>scarf/small scarf</div><div class="price">CHF 39.00</div><div class="cart"><svg viewBox="0 0 14 14" fill="none" stroke="#4a4d52" stroke-width="1.3"><path d="M1 2h2l2 7h7l1-5H4"/><circle cx="6" cy="12" r="1"/><circle cx="11" cy="12" r="1"/></svg>Add to cart</div></div>
<div class="product" style="left:834px;top:1618px"><div class="shot"><span role="img" aria-label="Navy floral scarf on a white shirt" style="background:linear-gradient(#b57a52 0 12%,#3a4160 12% 50%,#e9e9ea 50%)"></span></div><div class="name">Mirella triangular<br>scarf/small scarf</div><div class="price">CHF 39.00</div><div class="cart"><svg viewBox="0 0 14 14" fill="none" stroke="#4a4d52" stroke-width="1.3"><path d="M1 2h2l2 7h7l1-5H4"/><circle cx="6" cy="12" r="1"/><circle cx="11" cy="12" r="1"/></svg>Add to cart</div></div>
<div class="product" style="left:150px;top:1946px"><div class="shot"><span role="img" aria-label="Green patterned scarf on an ombré top" style="background:linear-gradient(#b57a52 0 12%,#9aa89a 12% 45%,#3a4654 45%)"></span></div><div class="name">Mirella triangular<br>scarf/small scarf</div><div class="price">CHF 39.00</div><div class="cart"><svg viewBox="0 0 14 14" fill="none" stroke="#4a4d52" stroke-width="1.3"><path d="M1 2h2l2 7h7l1-5H4"/><circle cx="6" cy="12" r="1"/><circle cx="11" cy="12" r="1"/></svg>Add to cart</div></div>
<div class="product" style="left:378px;top:1946px"><div class="shot"><span role="img" aria-label="Blue patterned scarf on a red cardigan" style="background:linear-gradient(#b57a52 0 12%,#46527a 12% 45%,#c42a3a 45%)"></span></div><div class="name">Mirella triangular<br>scarf/small scarf</div><div class="price">CHF 39.00</div><div class="cart"><svg viewBox="0 0 14 14" fill="none" stroke="#4a4d52" stroke-width="1.3"><path d="M1 2h2l2 7h7l1-5H4"/><circle cx="6" cy="12" r="1"/><circle cx="11" cy="12" r="1"/></svg>Add to cart</div></div>
<div class="product" style="left:607px;top:1946px"><div class="shot"><span role="img" aria-label="Pink floral scarf on a denim dress" style="background:linear-gradient(#b57a52 0 12%,#d9a2a5 12% 45%,#4f6a8a 45%)"></span></div><div class="name">Mirella triangular<br>scarf/small scarf</div><div class="price">CHF 39.00</div><div class="cart"><svg viewBox="0 0 14 14" fill="none" stroke="#4a4d52" stroke-width="1.3"><path d="M1 2h2l2 7h7l1-5H4"/><circle cx="6" cy="12" r="1"/><circle cx="11" cy="12" r="1"/></svg>Add to cart</div></div>
<div class="product" style="left:834px;top:1946px"><div class="shot"><span role="img" aria-label="Checked scarf on a light denim shirt" style="background:linear-gradient(#b57a52 0 12%,#3d5c9a 12% 40%,#7ea3cf 40%)"></span></div><div class="name">Mirella triangular<br>scarf/small scarf</div><div class="price">CHF 39.00</div><div class="cart"><svg viewBox="0 0 14 14" fill="none" stroke="#4a4d52" stroke-width="1.3"><path d="M1 2h2l2 7h7l1-5H4"/><circle cx="6" cy="12" r="1"/><circle cx="11" cy="12" r="1"/></svg>Add to cart</div></div>
<div class="btn" style="left:541px;top:2282px;width:120px;height:36px">Show all <svg viewBox="0 0 12 12" fill="none" stroke="#fff" stroke-width="1.3"><path d="M1 6h10M7 2l4 4-4 4"/></svg></div>

<div class="tile" style="left:16px;width:579px;background:linear-gradient(100deg,#d9dadb 0 45%,#a9804a 60%,#d45f8a 85%,#e7e7e7)" role="img" aria-label="Two colourful scarves hanging from a wooden branch">
  <h3 class="head" style="left:58px;top:182px">Story – Creation</h3>
  <p style="left:56px;top:222px">Each scarf begins with<br>carefully selected fabrics.<br>Colors, patterns and details are<br>combined to create a unique piece.</p>
</div>
<div class="tile" style="left:608px;width:577px;background:linear-gradient(100deg,#f2f2f2 0 40%,#e1cdb9 55%,#b7786a 75%,#e8ddd3)" role="img" aria-label="Rose floral scarf draped over a wooden ladder">
  <h3 class="head" style="left:54px;top:182px">Usage / Everyday</h3>
  <p style="left:53px;top:222px">Whether in everyday life, at the<br>office or on a walk – KOR-VADO<br>scarves bring color and<br>lightness to any outfit.</p>
</div>

<div class="abs unique"></div>
<div class="abs" style="left:470px;top:2905px;width:270px;height:380px;border-radius:40% 45% 30% 50%;background:radial-gradient(circle at 50% 45%,#ede3d6,#c9a590 70%,#8b6150)" role="img" aria-label="Cream floral scarf with tassels, tied in a knot"></div>
<div class="abs head unique-word">Uniqueness</div>
<p class="abs unique-note">Only 1 to 3 scarves are made from each fabric. Once sold, it remains unique.</p>

<h2 class="head section-title" style="top:3386px">Customer review</h2>
<div class="review" style="left:150px"><span class="avatar" style="background:linear-gradient(#b66a4e,#6d3f32)" role="img" aria-label="Customer photo"></span><div><b>Corinne</b><div class="stars"><svg viewBox="0 0 10 10"><path d="M5 0l1.5 3.2 3.5.4-2.6 2.4.7 3.5L5 7.8 1.9 9.5l.7-3.5L0 3.6l3.5-.4z" fill="#f0a830"/></svg><svg viewBox="0 0 10 10"><path d="M5 0l1.5 3.2 3.5.4-2.6 2.4.7 3.5L5 7.8 1.9 9.5l.7-3.5L0 3.6l3.5-.4z" fill="#f0a830"/></svg><svg viewBox="0 0 10 10"><path d="M5 0l1.5 3.2 3.5.4-2.6 2.4.7 3.5L5 7.8 1.9 9.5l.7-3.5L0 3.6l3.5-.4z" fill="#f0a830"/></svg><svg viewBox="0 0 10 10"><path d="M5 0l1.5 3.2 3.5.4-2.6 2.4.7 3.5L5 7.8 1.9 9.5l.7-3.5L0 3.6l3.5-.4z" fill="#f0a830"/></svg><svg viewBox="0 0 10 10"><path d="M5 0l1.5 3.2 3.5.4-2.6 2.4.7 3.5L5 7.8 1.9 9.5l.7-3.5L0 3.6l3.5-.4z" fill="#f0a830"/></svg>&nbsp; 2 years ago</div><p>I always receive compliments.</p></div></div>
<div class="review" style="left:454px"><span class="avatar" style="background:linear-gradient(#c9b08e,#5f6b7a)" role="img" aria-label="Customer photo"></span><div><b>Beatrice Hofer-Lang</b><div class="stars"><svg viewBox="0 0 10 10"><path d="M5 0l1.5 3.2 3.5.4-2.6 2.4.7 3.5L5 7.8 1.9 9.5l.7-3.5L0 3.6l3.5-.4z" fill="#f0a830"/></svg><svg viewBox="0 0 10 10"><path d="M5 0l1.5 3.2 3.5.4-2.6 2.4.7 3.5L5 7.8 1.9 9.5l.7-3.5L0 3.6l3.5-.4z" fill="#f0a830"/></svg><svg viewBox="0 0 10 10"><path d="M5 0l1.5 3.2 3.5.4-2.6 2.4.7 3.5L5 7.8 1.9 9.5l.7-3.5L0 3.6l3.5-.4z" fill="#f0a830"/></svg><svg viewBox="0 0 10 10"><path d="M5 0l1.5 3.2 3.5.4-2.6 2.4.7 3.5L5 7.8 1.9 9.5l.7-3.5L0 3.6l3.5-.4z" fill="#f0a830"/></svg><svg viewBox="0 0 10 10"><path d="M5 0l1.5 3.2 3.5.4-2.6 2.4.7 3.5L5 7.8 1.9 9.5l.7-3.5L0 3.6l3.5-.4z" fill="#f0a830"/></svg>&nbsp; 2 years ago</div><p>My favorite scarf – I already<br>own several.</p></div></div>
<div class="review" style="left:753px"><span class="avatar" style="background:linear-gradient(#c9707e,#e0b9a8)" role="img" aria-label="Customer photo"></span><div><b>Daniela</b><div class="stars"><svg viewBox="0 0 10 10"><path d="M5 0l1.5 3.2 3.5.4-2.6 2.4.7 3.5L5 7.8 1.9 9.5l.7-3.5L0 3.6l3.5-.4z" fill="#f0a830"/></svg><svg viewBox="0 0 10 10"><path d="M5 0l1.5 3.2 3.5.4-2.6 2.4.7 3.5L5 7.8 1.9 9.5l.7-3.5L0 3.6l3.5-.4z" fill="#f0a830"/></svg><svg viewBox="0 0 10 10"><path d="M5 0l1.5 3.2 3.5.4-2.6 2.4.7 3.5L5 7.8 1.9 9.5l.7-3.5L0 3.6l3.5-.4z" fill="#f0a830"/></svg><svg viewBox="0 0 10 10"><path d="M5 0l1.5 3.2 3.5.4-2.6 2.4.7 3.5L5 7.8 1.9 9.5l.7-3.5L0 3.6l3.5-.4z" fill="#f0a830"/></svg><svg viewBox="0 0 10 10"><path d="M5 0l1.5 3.2 3.5.4-2.6 2.4.7 3.5L5 7.8 1.9 9.5l.7-3.5L0 3.6l3.5-.4z" fill="#f0a830"/></svg>&nbsp; 2 years ago</div><p>My favorite scarf – I already<br>own several.</p></div></div>
<div class="abs dots"><i></i><i></i><i></i></div>

<h2 class="head section-title" style="top:3680px">Join the community</h2>
<p class="abs community-text">Find out when new models are released and where you can meet KOR-VADO in person.<br>I also share tips on how to wear the scarves.</p>
<div class="abs email">Enter your email <svg width="16" height="16" viewBox="0 0 16 16" fill="#4a4d52"><path d="M1 8l14-7-4 14-3-5z"/></svg></div>

<footer class="abs footer"></footer>
<div class="abs footer-brand"><i></i>KOR-VADO</div>
<h2 class="abs head footer-title">Discover your unique piece</h2>
<div class="abs footer-btn">Discover scarves now <svg width="12" height="12" viewBox="0 0 12 12" fill="none" stroke="#4a4d52" stroke-width="1.3"><path d="M1 6h10M7 2l4 4-4 4"/></svg></div>
<nav class="abs footer-links"><span>Seek</span><span>General terms and conditions of business</span><span>Data protection</span><span>Imprint</span><span>Shipping conditions</span><span>Refunds</span><span>Privacy settings</span></nav>
<div class="abs copyright">© 2026, KOR-VADO Powered by Storefront</div>
<div class="abs pay"><span style="background:#ffffff"></span><span style="background:#2a3b8f"></span><span style="background:#f2f2f2"></span><span style="background:#ffffff"></span><span style="background:#3b6fd1"></span></div>
<div class="abs chat"><svg width="18" height="18" viewBox="0 0 18 18"><circle cx="9" cy="9" r="7" fill="none" stroke="#fff" stroke-width="1.8"/></svg></div>

</body>
</html>
```